Design for a 4 screens iOS and Android app - "VelidMetra"

The app allows you to track your car gasoline refill ...
We need a design for the 4 screens of the app:
a) 1 form with 3 fields.
b) 1 simple list view
c) 1 summary view
d) 1 text page
2 "alerts" items are also to be designed.
No specific guidelines, nor logo or whatever.
It will be a free app distributed on iOS and Androïd.
We just want to make it looking nice & very usable for end users.
Target Market(s)
B2C app
Industry/Entity Type
Android

```html
<!DOCTYPE html>
<html lang="en">
<head>
<meta charset="utf-8">
<title>VelidMetra – app screens</title>
<link rel="stylesheet" href="https://fonts.googleapis.com/css2?family=Roboto:wght@400;500;700&display=swap">
<style>
:root{
  --stage:#000;
  --bar:#1f3ceb;
  --body:#4f68ea;
  --ink:#262626;
  --white:#fff;
  --muted:#a9a9a9;
  --link:#5a6cf0;
}
*{box-sizing:border-box;margin:0;padding:0}
html,body{width:1042px;height:1200px;overflow:hidden;background:var(--stage);font-family:'Roboto',sans-serif}
.screen{position:absolute;width:317px;height:563px;background:var(--body);overflow:hidden;color:var(--ink)}
.status{height:20px;background:var(--bar);color:var(--white);font-size:9px;display:flex;align-items:center;justify-content:space-between;padding:0 7px}
.status .mid{position:absolute;left:0;right:0;text-align:center;top:6px}
.status .batt{display:flex;align-items:center;gap:4px}
.status .cell{width:18px;height:8px;background:var(--white);border-radius:1px}
.tabs{height:52px;background:var(--bar);display:flex;position:relative}
.tab{flex:1;display:flex;align-items:center;justify-content:center}
.tab svg{width:24px;height:24px;fill:var(--white)}
.tab.active::after{content:"";position:absolute;bottom:0;width:105px;height:2px;background:var(--white)}
.tab.active{position:relative}
.about{position:absolute;right:17px;top:526px;color:var(--white);font-size:12.5px}
.field{position:absolute;left:57px;width:204px;height:30px;display:flex;background:var(--white);border-radius:2px;overflow:hidden}
.field .ico{width:32px;background:var(--ink);color:var(--white);display:flex;align-items:center;justify-content:center;font-size:12px}
.field .ico svg{width:14px;height:14px;fill:var(--white)}
.field .val{padding-left:7px;display:flex;align-items:center;font-size:12.5px}
.field .val.hint{color:var(--muted)}
.btn{position:absolute;left:57px;width:204px;height:30px;background:var(--ink);color:var(--white);font-size:12.5px;display:flex;align-items:center;justify-content:center;border-radius:2px}
.alert{position:absolute;left:56px;top:150px;width:205px;height:68px;background:var(--white);border-radius:3px;box-shadow:0 6px 14px rgba(0,0,0,.35);text-align:center;z-index:2}
.alert h3{font-size:12px;font-weight:500;margin-top:16px}
.alert p{color:var(--link);font-size:12px;margin-top:14px}
.month{position:absolute;left:10px;width:301px}
.month .label{display:inline-block;background:var(--ink);color:var(--white);font-weight:500;font-size:12.5px;height:25px;line-height:25px;padding:0 6px;border-radius:4px 4px 0 0}
.month .card{background:var(--white);border-top:3px solid var(--ink);height:79px;padding:3px 8px 0 7px;font-size:12px}
.month .row{display:flex;justify-content:space-between;height:18px;line-height:18px}
.month .row span:last-child{position:relative;top:-2px}
.entry{position:absolute;left:11px;width:292px;color:var(--white)}
.entry .date{font-weight:700;font-size:12px;padding-bottom:2px;border-bottom:1px solid var(--white)}
.entry .line{display:flex;justify-content:space-between;font-size:12px;margin-top:4px}
.entry .line span:last-child{position:relative;top:-4px}
.page{position:absolute;left:13px;top:104px;width:290px;background:var(--white);border-radius:2px;overflow:hidden;box-shadow:0 4px 10px rgba(0,0,0,.3)}
.page p{font-size:12.4px;line-height:15.4px;text-align:justify;padding:15px 11px 11px}
.page .close{background:var(--ink);color:var(--white);height:34px;display:flex;align-items:center;justify-content:center;font-size:12.5px}
</style>
</head>
<body>
<svg width="0" height="0" style="position:absolute">
  <defs>
    <symbol id="i-plus" viewBox="0 0 24 24"><path d="M9 2h6v7h7v6h-7v7H9v-7H2V9h7z"/></symbol>
    <symbol id="i-menu" viewBox="0 0 24 24"><rect x="1" y="3" width="22" height="3.5"/><rect x="1" y="10.3" width="22" height="3.5"/><rect x="1" y="17.5" width="22" height="3.5"/></symbol>
    <symbol id="i-chart" viewBox="0 0 24 24"><path d="M1 2h2v17h20v2H1z"/><path d="M4 18V11l4-5 5 6 3-3 5 4v5z"/></symbol>
    <symbol id="i-gauge" viewBox="0 0 24 24"><path d="M12 4A11 11 0 0 0 1 15v3h22v-3A11 11 0 0 0 12 4zm0 4l1.5 7h-3z"/></symbol>
    <symbol id="i-pump" viewBox="0 0 24 24"><path d="M4 2h10v19H4zm2 2v6h6V4zm10 4l4 3v8a2 2 0 0 1-4 0v-5h-1v-2h2v7h1v-7l-2-2z"/></symbol>
  </defs>
</svg>

<!-- Screen: add refill -->
<section class="screen" style="left:40px;top:34px">
  <div class="status"><span>●●●●● NOVA</span><span class="mid">4:21 PM</span><span class="batt">22% <span class="cell"></span></span></div>
  <nav class="tabs"><div class="tab active"><svg><use href="#i-plus"/></svg></div><div class="tab"><svg><use href="#i-menu"/></svg></div><div class="tab"><svg><use href="#i-chart"/></svg></div></nav>
  <div class="field" style="top:213px"><div class="ico"><svg><use href="#i-gauge"/></svg></div><div class="val">127500</div></div>
  <div class="field" style="top:248px"><div class="ico"><svg><use href="#i-pump"/></svg></div><div class="val hint">Liters</div></div>
  <div class="field" style="top:284px"><div class="ico">€</div><div class="val hint">Price</div></div>
  <div class="btn" style="top:322px">Save</div>
  <div class="about">About us »</div>
</section>

<!-- Screen: add refill with alert -->
<section class="screen" style="left:362px;top:34px">
  <div class="status"><span>●●●●● NOVA</span><span class="mid">4:21 PM</span><span class="batt">22% <span class="cell"></span></span></div>
  <nav class="tabs"><div class="tab active"><svg><use href="#i-plus"/></svg></div><div class="tab"><svg><use href="#i-menu"/></svg></div><div class="tab"><svg><use href="#i-chart"/></svg></div></nav>
  <div class="alert"><h3>Data Saved</h3><p>ok</p></div>
  <div class="field" style="top:213px"><div class="ico"><svg><use href="#i-gauge"/></svg></div><div class="val">127500</div></div>
  <div class="field" style="top:248px"><div class="ico"><svg><use href="#i-pump"/></svg></div><div class="val hint">Liters</div></div>
  <div class="field" style="top:284px"><div class="ico">€</div><div class="val hint">Price</div></div>
  <div class="btn" style="top:322px">Save</div>
  <div class="about">About us »</div>
</section>

<!-- Screen: monthly summary -->
<section class="screen" style="left:685px;top:34px">
  <div class="status"><span>●●●●● NOVA</span><span class="mid">4:21 PM</span><span class="batt">22% <span class="cell"></span></span></div>
  <nav class="tabs"><div class="tab"><svg><use href="#i-plus"/></svg></div><div class="tab active"><svg><use href="#i-menu"/></svg></div><div class="tab"><svg><use href="#i-chart"/></svg></div></nav>
  <div class="month" style="top:88px"><span class="label">Fevrier 2016</span><div class="card">
    <div class="row"><span>Total cost</span><span>570.58 €</span></div>
    <div class="row"><span>mileage</span><span>7500 km</span></div>
    <div class="row"><span>Full tanks</span><span>11</span></div>
    <div class="row"><span>Consumption</span><span>6.5 l</span></div></div></div>
  <div class="month" style="top:203px"><span class="label">Janvier 2016</span><div class="card">
    <div class="row"><span>Total cost</span><span>241.46 €</span></div>
    <div class="row"><span>mileage</span><span>2770 km</span></div>
    <div class="row"><span>Full tanks</span><span>4</span></div>
    <div class="row"><span>Consumption</span><span>6.1 l</span></div></div></div>
  <div class="month" style="top:317px"><span class="label">Fevrier 2016</span><div class="card">
    <div class="row"><span>Total cost</span><span>180 €</span></div>
    <div class="row"><span>mileage</span><span>1911 km</span></div>
    <div class="row"><span>Full tanks</span><span>3</span></div>
    <div class="row"><span>Consumption</span><span>6.2 l</span></div></div></div>
  <div class="about">About us »</div>
</section>

<!-- Screen: refill list -->
<section class="screen" style="left:199px;top:603px">
  <div class="status"><span>●●●●● NOVA</span><span class="mid">4:21 PM</span><span class="batt">22% <span class="cell"></span></span></div>
  <nav class="tabs"><div class="tab"><svg><use href="#i-plus"/></svg></div><div class="tab"><svg><use href="#i-menu"/></svg></div><div class="tab active"><svg><use href="#i-chart"/></svg></div></nav>
  <div class="entry" style="top:97px"><div class="date">15 Fevrier 2016&nbsp; 14:24</div><div class="line"><span>127500 km</span><span>570.58 €</span></div></div>
  <div class="entry" style="top:155px"><div class="date">15 Fevrier 2016&nbsp; 14:24</div><div class="line"><span>127500 km</span><span>570.58 €</span></div></div>
  <div class="entry" style="top:207px"><div class="date">15 Fevrier 2016&nbsp; 14:24</div><div class="line"><span>127500 km</span><span>570.58 €</span></div></div>
  <div class="entry" style="top:261px"><div class="date">15 Fevrier 2016&nbsp; 14:24</div><div class="line"><span>127500 km</span><span>570.58 €</span></div></div>
  <div class="entry" style="top:313px"><div class="date">15 Fevrier 2016&nbsp; 14:24</div><div class="line"><span>127500 km</span><span>570.58 €</span></div></div>
  <div class="entry" style="top:367px"><div class="date">15 Fevrier 2016&nbsp; 14:24</div><div class="line"><span>127500 km</span><span>570.58 €</span></div></div>
  <div class="entry" style="top:419px"><div class="date">15 Fevrier 2016&nbsp; 14:24</div><div class="line"><span>127500 km</span><span>570.58 €</span></div></div>
  <div class="entry" style="top:471px"><div class="date">15 Fevrier 2016&nbsp; 14:24</div><div class="line"><span>127500 km</span><span>570.58 €</span></div></div>
  <div class="entry" style="top:523px"><div class="date">15 Fevrier 2016&nbsp; 14:24</div><div class="line"><span>127500 km</span><span>570.58 €</span></div></div>
</section>

<!-- Screen: about text -->
<section class="screen" style="left:522px;top:603px">
  <div class="status"><span>●●●●● NOVA</span><span class="mid">4:21 PM</span><span class="batt">22% <span class="cell"></span></span></div>
  <nav class="tabs"><div class="tab"><svg><use href="#i-plus"/></svg></div><div class="tab"><svg><use href="#i-menu"/></svg></div><div class="tab active"><svg><use href="#i-chart"/></svg></div></nav>
  <div class="page">
    <p>Excitavit hic ardor milites per municipia plurima, quae isdem conterminant, dispositos et castella, sed quisque serpentes Latius pro viribus repellere moliens, munc globis confertos, aliquotiens et dispersos multitudine superabatur ingenti, quae nata et educata inter editos recurvosque ambitus montium eos ut, loca plana persultat et mollia, missilibus obvios eminus lacessens et ululatu truci perterens.</p>
    <div class="close">Close</div>
  </div>
</section>
</body>
</html>
```